Calendar Ad / Flyer

Our law firm needs a calendar ad to place in a local calendar.
THE DEADLINE IS THIS THURSDAY 06/28/2018.

Attached is the ad used in last years calendar. A few notes on this...
**. This is by no means the model to follow.
Please be creative and do what makes more sense marketing wise.
1. Need to update the color scheme which corresponds to the new website at morvanlegal.net
2. The "MORVAN LEGAL | STANDING FIRM FOR YOUR FUTURE" should be put at the top and made larger
3. "KNOWN AND TRUSTED IN OUR COMMUNITY FOR OVER 21 YEARS" should be changed to "KNOWN AND TRUSTED IN OUR COMMUNITY FOR OVER 22 YEARS"
4. "Dorian K. Morvan, Esq." should be made larger and better positioned.
5. Under the list of practices, it should be changed to have:
"Personal Injury, Legal Malpractice, Unlicensed Contractors, Medical Malpractice, Civil Litigation"
6. Contact information (i.e. contact number, website, and address) should be better positioned
7. Placement of endorsement logos should stand out more.
8. New picture of head attorney is attached.

Last but not least... Give it your best shot!

```html
<!DOCTYPE html>
<html lang="en">
<head>
<meta charset="utf-8">
<title>Morvan Legal – Calendar Ad</title>
<link href="https://fonts.googleapis.com/css2?family=Montserrat:wght@500&family=Roboto:ital,wght@0,300;0,400;0,500;1,700&display=swap" rel="stylesheet">
<style>
  :root {
    --gold: #c6a56f;
    --ink: #151515;
    --panel: #161616;
    --paper: #ffffff;
    --muted: #d9d9d9;
    --rule: #4a4a4a;
    --canvas: #e7e7e9;
    --badge-red: #8e1c1c;
    --badge-blue: #2f7cc0;
    --portrait-light: #a88a78;
    --portrait-mid: #5b5552;
  }
  * { margin: 0; padding: 0; box-sizing: border-box; }
  html, body {
    width: 1200px; height: 1200px; overflow: hidden;
    background: var(--canvas);
  }
  .ad {
    position: absolute; left: 50px; top: 172px;
    width: 1100px; height: 857px;
    box-shadow: 0 10px 24px rgba(0,0,0,.25);
  }
  .ad svg { display: block; width: 100%; height: 100%; }

  .stop-gold { stop-color: var(--gold); }
  .stop-gold-clear { stop-color: var(--gold); stop-opacity: 0; }
  .stop-rule { stop-color: var(--rule); }
  .stop-rule-clear { stop-color: var(--rule); stop-opacity: 0; }
  .stop-portrait-light { stop-color: var(--portrait-light); }
  .stop-portrait-mid { stop-color: var(--portrait-mid); }
  .stop-portrait-dark { stop-color: var(--panel); }

  .stripes-left rect { fill: url(#stripe-left); }
  .stripes-right rect { fill: url(#stripe-right); }
  .practice-rules rect { fill: url(#rule-fade); }
  .portrait-area { fill: url(#portrait-tone); }

  .brand-name { font-family: "Montserrat", sans-serif; font-weight: 500; font-size: 50px; letter-spacing: 5px; fill: var(--gold); }
  .tagline { font-family: "Roboto", sans-serif; font-weight: 500; font-size: 18px; fill: var(--ink); }
  .headline { font-family: "Roboto", sans-serif; font-weight: 500; font-size: 24px; fill: var(--gold); }
  .years-small { font-family: "Roboto", sans-serif; font-weight: 400; font-size: 24px; fill: var(--muted); }
  .years-big { font-family: "Roboto", sans-serif; font-weight: 400; font-size: 38px; fill: var(--muted); }
  .practice { font-family: "Roboto", sans-serif; font-weight: 400; font-size: 22px; fill: var(--muted); }
  .attorney { font-family: "Roboto", sans-serif; font-weight: 700; font-style: italic; font-size: 44px; fill: var(--ink); }
  .attorney-suffix { font-size: 28px; font-style: normal; }
  .availability { font-family: "Roboto", sans-serif; font-weight: 300; font-size: 20px; fill: var(--muted); }
  .phone { font-family: "Roboto", sans-serif; font-weight: 500; font-size: 46px; fill: var(--gold); }
  .website { font-family: "Roboto", sans-serif; font-weight: 400; font-size: 28px; letter-spacing: 4px; fill: var(--gold); }
</style>
</head>
<body>
<div class="ad">
  <svg viewBox="0 0 994 774" xmlns="http://www.w3.org/2000/svg">
    <defs>
      <linearGradient id="stripe-left" x1="0" y1="0" x2="1" y2="0">
        <stop offset="0" class="stop-gold"/>
        <stop offset="1" class="stop-gold-clear"/>
      </linearGradient>
      <linearGradient id="stripe-right" x1="1" y1="0" x2="0" y2="0">
        <stop offset="0" class="stop-gold"/>
        <stop offset="1" class="stop-gold-clear"/>
      </linearGradient>
      <linearGradient id="rule-fade" x1="0" y1="0" x2="1" y2="0">
        <stop offset="0" class="stop-rule"/>
        <stop offset="1" class="stop-rule-clear"/>
      </linearGradient>
      <radialGradient id="portrait-tone" cx="0.6" cy="0.45" r="0.6">
        <stop offset="0" class="stop-portrait-light"/>
        <stop offset="0.45" class="stop-portrait-mid"/>
        <stop offset="1" class="stop-portrait-dark"/>
      </radialGradient>
    </defs>

    <!-- Header -->
    <rect class="header" x="0" y="0" width="994" height="238" fill="#ffffff"/>
    <g class="stripes-left">
      <rect x="0" y="111" width="250" height="1.5"/>
      <rect x="0" y="121" width="250" height="1.5"/>
      <rect x="0" y="131" width="250" height="1.5"/>
      <rect x="0" y="141" width="250" height="2"/>
      <rect x="0" y="150" width="250" height="4"/>
      <rect x="0" y="160" width="250" height="4"/>
      <rect x="0" y="170" width="250" height="4"/>
      <rect x="0" y="181" width="250" height="2"/>
      <rect x="0" y="191" width="250" height="1.5"/>
    </g>
    <g class="stripes-right">
      <rect x="744" y="111" width="250" height="1.5"/>
      <rect x="744" y="121" width="250" height="1.5"/>
      <rect x="744" y="131" width="250" height="1.5"/>
      <rect x="744" y="141" width="250" height="2"/>
      <rect x="744" y="150" width="250" height="4"/>
      <rect x="744" y="160" width="250" height="4"/>
      <rect x="744" y="170" width="250" height="4"/>
      <rect x="744" y="181" width="250" height="2"/>
      <rect x="744" y="191" width="250" height="1.5"/>
    </g>
    <text class="brand-name" x="497" y="192" text-anchor="middle">MORVAN LEGAL</text>
    <text class="tagline" x="497" y="216" text-anchor="middle">STANDING FIRM FOR YOUR FUTURE</text>

    <!-- Main panel -->
    <rect class="main-panel" x="0" y="238" width="994" height="354" fill="#161616"/>
    <g role="img" aria-label="Portrait photograph of the head attorney in a grey suit">
      <rect class="portrait-area" x="406" y="238" width="588" height="354"/>
    </g>

    <text class="headline" x="73" y="296">KNOWN AND TRUSTED IN OUR COMMUNITY</text>
    <text x="73" y="343"><tspan class="years-small">FOR </tspan><tspan class="years-big">OVER 22 YEARS</tspan></text>

    <g class="practice-list">
      <g class="practice-rules">
        <rect x="134" y="410" width="440" height="1.2"/>
        <rect x="134" y="446" width="440" height="1.2"/>
        <rect x="134" y="481" width="440" height="1.2"/>
        <rect x="134" y="516" width="440" height="1.2"/>
      </g>
      <g class="ticks" fill="none" stroke="#c6a56f" stroke-width="3.5" stroke-linecap="round" stroke-linejoin="round">
        <path d="M105 392 l6 6 l12 -14"/>
        <path d="M105 428 l6 6 l12 -14"/>
        <path d="M105 464 l6 6 l12 -14"/>
        <path d="M105 499 l6 6 l12 -14"/>
        <path d="M105 535 l6 6 l12 -14"/>
      </g>
      <text class="practice" x="134" y="401">Personal Injury</text>
      <text class="practice" x="134" y="437">Legal Malpractice</text>
      <text class="practice" x="134" y="473">Unlicensed Contractors</text>
      <text class="practice" x="134" y="508">Medical Malpractice</text>
      <text class="practice" x="134" y="544">Civil Litigation</text>
    </g>

    <!-- Footer -->
    <rect class="footer" x="0" y="592" width="994" height="182" fill="#ffffff"/>
    <polygon class="name-band" points="0,592 994,592 994,660 412,660 361,611 0,611" fill="#c6a56f"/>
    <polygon class="contact-block" points="0,611 361,611 531,774 0,774" fill="#161616"/>
    <polygon class="contact-edge" points="361,611 375,611 545,774 531,774" fill="#bdbdbd"/>

    <text class="attorney" x="956" y="645" text-anchor="end">Dorian K. Morvan,<tspan class="attorney-suffix"> Esq.</tspan></text>

    <text class="availability" x="73" y="650">We’re available 24/7</text>
    <text class="phone" x="70" y="701">(555) 014-7720</text>
    <text class="website" x="73" y="737">morvanlegal.net</text>

    <g class="endorsements">
      <circle cx="554" cy="710" r="24" fill="#8e1c1c" stroke="#c6a56f" stroke-width="3"/>
      <rect x="617" y="690" width="54" height="40" fill="#c41200"/>
      <rect x="708" y="688" width="52" height="44" rx="3" fill="#7a6a48"/>
      <rect x="790" y="694" width="78" height="32" rx="4" fill="#2f7cc0"/>
      <circle cx="927" cy="708" r="24" fill="#ffffff" stroke="#2f7cc0" stroke-width="5"/>
    </g>
  </svg>
</div>
</body>
</html>
```